Bright Acorns Business Card Design

Bright Acorns - Cultivating Natural Play Spaces

Bright Acorns is a company that focuses on promoting the design, construction, consultation and support of natural, creative and organic play spaces for Early Childhood and learning environments.

We need a professional Business Card designed that is unique modern and creative. The Philosophy of the company is nostalgic so the business and will need to reflect this but also reflect that our ideas are modern and cutting edge.

The business card will need to be a talking point, by either having a unique size, quality and/or placement of logo or other quality.

I am more interested in using natural recycled paper, as this would reflect the philosophy of the company, but I open to seeing colour used creatively.
Updates

Hi Designers, Apologies, Could you please add www.brightacorns.com.au to the business card. Thanks very much.

Hi All, Thank you all for your submission thus far. Please note the fonts for used in the logo are: Ostrich Sans Black and Archer Semi Bold. If these could be considered for contact details, my name etc. Also please show the design on a recycled brown card if possible as this will be the type of card I will use when printing. Thanks so much.

Target Market(s)

Child Care Providers, Play Industry Professionals

Industry/Entity Type

Business

Contact Information for Business Card

Bright Acorns
Nurturing Outdoor Play Places
Marlene Okafor
0419 862 304
marlene@brightacorns.com.au

Font styles to use
Sans Serif

Requirements
Must have
• The Logo and the Details plus the below phrase
• Bright Acorns - Cultivating Natural Play Spaces
Nice to have
• A bit of colour, but not too much colour.
Should not have
• Not to have a white background, recycled brown card only

```html
<!DOCTYPE html>
<html lang="en">
<head>
<meta charset="utf-8">
<title>Bright Acorns Business Card Design</title>
<link rel="stylesheet" href="https://fonts.googleapis.com/css2?family=Zilla+Slab:wght@400;500&display=swap">
<style>
  :root {
    --backdrop: #1b1612;
    --kraft: #a98c6e;
    --ink: #1c1714;
    --serif: "Zilla Slab", Georgia, serif;
  }
  html, body {
    margin: 0;
    padding: 0;
    width: 1200px;
    height: 1000px;
    overflow: hidden;
    background: var(--backdrop);
  }
  .canvas {
    position: relative;
    width: 1200px;
    height: 1000px;
  }
  .card {
    position: absolute;
    left: 236px;
    width: 728px;
    height: 416px;
    background: var(--kraft);
    color: var(--ink);
    font-family: var(--serif);
    text-align: center;
  }
  .card--front { top: 72px; }
  .card--back { top: 512px; }

  .brand-dot {
    position: absolute;
    left: 50%;
    border-radius: 50%;
    background: var(--ink);
    transform: translateX(-50%);
  }
  .card--front .brand-dot { top: 96px; width: 64px; height: 64px; }

  .holder-name {
    position: absolute;
    top: 194px;
    left: 0;
    right: 0;
    margin: 0;
    font-size: 23px;
    font-weight: 500;
    letter-spacing: 2px;
    text-transform: uppercase;
  }
  .holder-rule {
    position: absolute;
    top: 229px;
    left: 334px;
    width: 60px;
    height: 1px;
    background: var(--ink);
  }
  .contact-list {
    position: absolute;
    top: 250px;
    left: 0;
    right: 0;
    margin: 0;
    padding: 0;
    list-style: none;
    font-size: 19px;
    line-height: 28px;
    letter-spacing: 1px;
  }

  .card--back .brand-dot { top: 92px; width: 110px; height: 110px; }
  .brand-name {
    position: absolute;
    top: 246px;
    left: 0;
    right: 0;
    margin: 0;
    font-size: 46px;
    font-weight: 500;
    letter-spacing: 2px;
    text-transform: uppercase;
    line-height: 1;
  }
  .tagline {
    position: absolute;
    top: 292px;
    left: 0;
    right: 0;
    margin: 0;
    font-size: 16px;
    line-height: 19px;
    letter-spacing: 1px;
    text-transform: uppercase;
  }
  .flourish {
    position: absolute;
    top: 336px;
    left: 314px;
    width: 100px;
    height: 6px;
    background: linear-gradient(90deg, transparent, rgba(28,23,20,.6), transparent);
  }
</style>
</head>
<body>
<main class="canvas">
  <section class="card card--front">
    <div class="brand-dot"></div>
    <h1 class="holder-name">Marlene Okafor</h1>
    <div class="holder-rule"></div>
    <ul class="contact-list">
      <li>0419 862 304</li>
      <li>marlene@brightacorns.com.au</li>
      <li>www.brightacorns.com.au</li>
    </ul>
  </section>

  <section class="card card--back">
    <div class="brand-dot"></div>
    <h2 class="brand-name">Bright Acorns</h2>
    <p class="tagline">Nurturing<br>Outdoor Play Places</p>
    <div class="flourish" role="img" aria-label="Small decorative scroll flourish"></div>
  </section>
</main>
</body>
</html>
```